Banner Ad Design Project

I just launched an affiliate program for my company (Ridgeline Academy), and I need some web ads and banners created. 6 in total.Here are the specs for the ads:
W120XH90- Small Web Ad
W120XH160- Big Web Ad
W468XH60- Full Banner Ad
W250XH250- Big Banner Ad
W125XH125- Samll Square Ad
W160XH600- Wide Skyscraper
I've uploaded one example I made hower I am looking for a more professional look. You'll also see a few flyers I've uploaded. These will get you an idea of the product.
Here is what I am looking to achieve and a little background on my product:
RIDGELINE Academy’s first course, ‘Ready for Shifts’ is a 30 minute interactive training and certification course specifically designed for teens and young adults to better prepare them for the workplace. The training is based on employer feedback, delivered on a peer-to-peer level, industry nonspecific, mobile ready and covers the following challenges:
• Work Ethic
• Social Media
• Cell Phone Issues
• Communication and Manners Matter
• Hygiene and more.
These ads are to catch the eyes of bosses, supervisors and managers. Basically anyone who is looking to improve workplace performance. Our website is www.ridgelineacademy-example.com. Please look it over for our branding. Thanks so much!
ps- Please make 1/2 static banners and 1/2 animated (gif of flash) banner.
Target Market(s)
Bosses, supervisors and managers. Anyone who employees teenagers and young adults and is looking to train them to better serve their customers.
Industry/Entity Type
Training
Look and feel

```html
<!DOCTYPE html>
<html lang="en">
<head>
<meta charset="utf-8">
<title>Ridgeline Academy – Affiliate Banner Set</title>
<link rel="stylesheet" href="https://fonts.googleapis.com/css2?family=Fjalla+One&family=Fira+Sans+Condensed:wght@500&family=Great+Vibes&display=swap">
<style>
  :root{
    --board-light:#b4b1b0;
    --board-dark:#7d7b7b;
    --blue:#1b55a8;
    --blue-deep:#0c3483;
    --red:#c2161e;
    --red-deep:#86070d;
    --yellow:#ffe43c;
    --yellow-deep:#f2b800;
    --white:#ffffff;
    --brand:#1c4a9c;
    --photo-a:#c9a58c;
    --photo-b:#3d6fa8;
  }
  *{box-sizing:border-box;margin:0;padding:0}
  html,body{width:1200px;height:774px;overflow:hidden}
  body{
    background:radial-gradient(ellipse at 55% 35%,var(--board-light),var(--board-dark) 85%);
    position:relative;
    font-family:"Fira Sans Condensed",Arial,sans-serif;
    color:var(--white);
  }
  .ad{position:absolute;overflow:hidden;box-shadow:0 2px 6px rgba(0,0,0,.35)}
  .ad > *{position:absolute}
  .blue-field{background:radial-gradient(ellipse at 50% 30%,var(--blue),var(--blue-deep) 90%)}
  .red-field{background:radial-gradient(ellipse at 50% 30%,var(--red),var(--red-deep) 90%)}
  .white-field{background:var(--white)}
  .fill{left:0;top:0;width:100%;height:100%}
  .brand{
    font-family:"Fjalla One",Arial,sans-serif;color:var(--brand);
    text-align:center;line-height:1.05;white-space:nowrap;
  }
  .script{font-family:"Great Vibes",cursive;line-height:1;white-space:nowrap}
  .headline{font-family:"Fjalla One",Arial,sans-serif;color:var(--yellow);line-height:1;white-space:nowrap;text-shadow:0 1px 2px rgba(0,0,0,.45)}
  .copy{font-weight:500;text-align:center;line-height:1.3}
  .bullets{list-style:none;font-weight:500;white-space:nowrap}
  .bullets li::before{content:"\2714\00a0"}
  .center{text-align:center}
  .btn{
    display:flex;align-items:center;justify-content:center;gap:6px;
    font-family:"Fira Sans Condensed",Arial,sans-serif;font-weight:500;
    border-radius:4px;white-space:nowrap;box-shadow:0 2px 3px rgba(0,0,0,.4);
  }
  .btn-red{background:linear-gradient(var(--red),var(--red-deep));color:var(--white)}
  .btn-yellow{background:linear-gradient(var(--yellow),var(--yellow-deep));color:#111}
  .btn .arrow{display:inline-block;border-radius:50%;background:var(--white);color:var(--red);font-size:.7em;line-height:1.6;width:1.6em;text-align:center}
  .photo{background:linear-gradient(160deg,var(--photo-a),var(--photo-b));opacity:.9}
  .stripe{left:0;width:100%}
</style>
</head>
<body>

<!-- Wide skyscraper, blue -->
<section class="ad blue-field" style="left:43px;top:30px;width:160px;height:600px">
  <div class="white-field" style="left:0;top:0;width:160px;height:128px"></div>
  <div class="brand" style="left:0;top:40px;width:160px;font-size:22px">RIDGELINE<br>Academy</div>
  <div class="stripe" style="top:128px;height:8px;background:var(--red)"></div>
  <div class="script center" style="left:0;top:142px;width:160px;font-size:46px">Online</div>
  <div class="script center" style="left:0;top:190px;width:160px;font-size:42px">Training</div>
  <div class="headline center" style="left:0;top:238px;width:160px;font-size:31px">TEACHING</div>
  <div class="headline center" style="left:0;top:274px;width:160px;font-size:25px">WORKPLACE</div>
  <p class="copy" style="left:6px;top:312px;width:148px;font-size:14px">skills to teens &amp; young adults, transforming them into valued employees &amp; customer service ambassadors.</p>
  <div class="photo" role="img" aria-label="Group of smiling young adult students" style="left:0;top:432px;width:160px;height:168px"></div>
  <div class="btn btn-red" style="left:9px;top:555px;width:146px;height:33px;font-size:17px">Free Preview! <span class="arrow">&#10140;</span></div>
</section>

<!-- Wide skyscraper, red -->
<section class="ad red-field" style="left:226px;top:30px;width:160px;height:600px">
  <div class="white-field" style="left:0;top:0;width:160px;height:142px"></div>
  <div class="brand" style="left:0;top:48px;width:160px;font-size:22px">RIDGELINE<br>Academy</div>
  <div class="stripe" style="top:142px;height:8px;background:var(--blue)"></div>
  <div class="script center" style="left:0;top:156px;width:160px;font-size:50px">Online</div>
  <div class="headline center" style="left:0;top:212px;width:160px;font-size:30px">EMPLOYEE</div>
  <div class="headline center" style="left:0;top:248px;width:160px;font-size:34px">TRAINING</div>
  <ul class="bullets" style="left:8px;top:296px;font-size:13.5px;line-height:21px">
    <li>Covering Social Media.</li><li>Texting &amp; Cell Phones.</li><li>Grooming &amp; Hygiene.</li>
  </ul>
  <div class="photo" role="img" aria-label="Two young professional women in business attire" style="left:0;top:372px;width:160px;height:228px"></div>
  <div class="btn btn-yellow" style="left:12px;top:553px;width:145px;height:32px;font-size:17px">Free Preview!</div>
</section>

<!-- Wide skyscraper, logo at base -->
<section class="ad blue-field" style="left:404px;top:30px;width:160px;height:600px">
  <div class="script center" style="left:0;top:12px;width:160px;font-size:46px">Online</div>
  <div class="script center" style="left:0;top:58px;width:160px;font-size:42px">Training</div>
  <div class="headline center" style="left:0;top:102px;width:160px;font-size:33px">TEACHING</div>
  <div class="headline center" style="left:0;top:140px;width:160px;font-size:26px">WORKPLACE</div>
  <p class="copy" style="left:6px;top:182px;width:148px;font-size:14px">skills to teens &amp; young adults, transforming them into valued employees &amp; customer service ambassadors.</p>
  <div class="btn btn-yellow" style="left:13px;top:302px;width:134px;height:32px;font-size:17px">Free Preview!</div>
  <div class="photo" role="img" aria-label="Group of young adult students holding books" style="left:0;top:344px;width:160px;height:130px"></div>
  <svg style="left:0;top:466px" width="160" height="134" viewBox="0 0 160 134" aria-hidden="true">
    <path d="M0 22 Q80 -8 160 22 V134 H0Z" fill="#c2161e"/>
    <path d="M0 30 Q80 2 160 30 V134 H0Z" fill="#fff"/>
  </svg>
  <div class="brand" style="left:0;top:530px;width:160px;font-size:22px">RIDGELINE<br>Academy</div>
</section>

<!-- Big banner 250x250, curve right -->
<section class="ad blue-field" style="left:582px;top:46px;width:250px;height:250px">
  <svg style="left:0;top:0" width="250" height="250" viewBox="0 0 250 250" aria-hidden="true">
    <path d="M170 0 Q130 120 150 250 H250 V0Z" fill="#c2161e"/>
    <path d="M178 0 Q138 120 158 250 H250 V0Z" fill="#fff"/>
  </svg>
  <div class="brand" style="left:165px;top:18px;width:80px;font-size:13px">RIDGELINE<br>Academy</div>
  <div class="photo" role="img" aria-label="Three smiling students with notebooks" style="left:140px;top:70px;width:110px;height:180px"></div>
  <div class="script" style="left:10px;top:8px;font-size:36px">Online</div>
  <div class="script" style="left:10px;top:44px;font-size:34px">Training</div>
  <div class="headline" style="left:6px;top:88px;font-size:26px">TEACHING</div>
  <div class="headline" style="left:6px;top:118px;font-size:21px">WORKPLACE</div>
  <div class="headline" style="left:6px;top:146px;font-size:34px">SKILLS</div>
  <ul class="bullets" style="left:6px;top:186px;font-size:12.5px;line-height:20px">
    <li>Covering Social Media.</li><li>Texting &amp; Cell Phones.</li><li>Grooming &amp; Hygiene.</li>
  </ul>
  <div class="btn btn-yellow" style="left:143px;top:216px;width:98px;height:24px;font-size:13px">Free Preview!</div>
</section>

<!-- Big banner 250x250, white header -->
<section class="ad blue-field" style="left:851px;top:46px;width:250px;height:250px">
  <svg style="left:0;top:0" width="250" height="120" viewBox="0 0 250 120" aria-hidden="true">
    <path d="M0 0 H250 V40 Q120 70 0 100Z" fill="#c2161e"/>
    <path d="M0 0 H250 V32 Q120 62 0 92Z" fill="#fff"/>
  </svg>
  <div class="brand" style="left:10px;top:18px;width:80px;font-size:14px">RIDGELINE<br>Academy</div>
  <div class="photo" role="img" aria-label="Three young adult students standing together" style="left:148px;top:0;width:102px;height:250px"></div>
  <div class="script" style="left:6px;top:100px;font-size:24px">Online Training</div>
  <div class="headline" style="left:6px;top:126px;font-size:31px">TEACHING</div>
  <div class="headline" style="left:6px;top:163px;font-size:16px">WORKPLACE SKILLS</div>
  <ul class="bullets" style="left:6px;top:188px;font-size:12.5px;line-height:20px">
    <li>Covering Social Media.</li><li>Texting &amp; Cell Phones.</li><li>Grooming &amp; Hygiene.</li>
  </ul>
  <div class="btn btn-red" style="left:147px;top:219px;width:98px;height:24px;font-size:13px">Free Preview! <span class="arrow">&#10140;</span></div>
</section>

<!-- Big web ad 120x160, yellow button -->
<section class="ad blue-field" style="left:582px;top:320px;width:120px;height:160px">
  <div class="script center" style="left:0;top:2px;width:120px;font-size:18px">Online Training</div>
  <div class="headline center" style="left:0;top:18px;width:120px;font-size:23px">TEACHING</div>
  <div class="headline center" style="left:0;top:45px;width:120px;font-size:11.5px">WORKPLACE SKILLS</div>
  <ul class="bullets" style="left:4px;top:60px;font-size:10px;line-height:16px">
    <li>Covering Social Media.</li><li>Texting &amp; Cell Phones.</li><li>Grooming &amp; Hygiene.</li>
  </ul>
  <div class="white-field" style="left:0;top:110px;width:120px;height:50px"></div>
  <div class="photo" role="img" aria-label="Three smiling students" style="left:50px;top:106px;width:70px;height:40px"></div>
  <div class="brand" style="left:2px;top:126px;width:50px;font-size:8px">RIDGELINE<br>Academy</div>
  <div class="btn btn-yellow" style="left:54px;top:139px;width:56px;height:14px;font-size:8px">Free Preview!</div>
</section>

<!-- Big web ad 120x160, red button -->
<section class="ad blue-field" style="left:712px;top:320px;width:120px;height:160px">
  <div class="script center" style="left:0;top:2px;width:120px;font-size:18px">Online Training</div>
  <div class="headline center" style="left:0;top:20px;width:120px;font-size:24px">TEACHING</div>
  <div class="headline center" style="left:0;top:47px;width:120px;font-size:11.5px">WORKPLACE SKILLS</div>
  <ul class="bullets" style="left:10px;top:62px;font-size:10px;line-height:16px">
    <li>Covering Social Media.</li><li>Texting &amp; Cell Phones.</li><li>Grooming &amp; Hygiene.</li>
  </ul>
  <div class="white-field" style="left:0;top:112px;width:120px;height:48px"></div>
  <div class="photo" role="img" aria-label="Group of young students" style="left:55px;top:108px;width:65px;height:36px"></div>
  <div class="brand" style="left:2px;top:128px;width:48px;font-size:8px">RIDGELINE<br>Academy</div>
  <div class="btn btn-red" style="left:50px;top:139px;width:62px;height:14px;font-size:8px">Free Preview! <span class="arrow">&#10140;</span></div>
</section>

<!-- Small square 125x125, white header -->
<section class="ad blue-field" style="left:851px;top:320px;width:125px;height:125px">
  <svg style="left:0;top:0" width="125" height="60" viewBox="0 0 125 60" aria-hidden="true">
    <path d="M0 0 H125 V20 Q60 36 0 50Z" fill="#c2161e"/>
    <path d="M0 0 H125 V16 Q60 32 0 46Z" fill="#fff"/>
  </svg>
  <div class="brand" style="left:4px;top:6px;width:46px;font-size:8px">RIDGELINE<br>Academy</div>
  <div class="photo" role="img" aria-label="Three young students standing" style="left:70px;top:0;width:55px;height:112px"></div>
  <div class="script" style="left:3px;top:50px;font-size:13px">Online Training</div>
  <div class="headline" style="left:3px;top:63px;font-size:16px">TEACHING</div>
  <div class="headline" style="left:3px;top:80px;font-size:8.5px">WORKPLACE SKILLS</div>
  <ul class="bullets" style="left:3px;top:90px;font-size:6.5px;line-height:9px">
    <li>Covering Social Media.</li><li>Texting &amp; Cell Phones.</li><li>Grooming &amp; Hygiene.</li>
  </ul>
  <div class="btn btn-red" style="left:74px;top:110px;width:48px;height:11px;font-size:6.5px">Free Preview! <span class="arrow">&#10140;</span></div>
</section>

<!-- Small square 125x125, curve right -->
<section class="ad blue-field" style="left:1004px;top:320px;width:125px;height:125px">
  <svg style="left:0;top:0" width="125" height="125" viewBox="0 0 125 125" aria-hidden="true">
    <path d="M86 0 Q64 60 74 125 H125 V0Z" fill="#c2161e"/>
    <path d="M90 0 Q68 60 78 125 H125 V0Z" fill="#fff"/>
  </svg>
  <div class="brand" style="left:82px;top:8px;width:42px;font-size:7px">RIDGELINE<br>Academy</div>
  <div class="photo" role="img" aria-label="Smiling students with books" style="left:70px;top:32px;width:55px;height:76px"></div>
  <div class="script" style="left:4px;top:4px;font-size:18px">Online</div>
  <div class="script" style="left:4px;top:20px;font-size:17px">Training</div>
  <div class="headline" style="left:3px;top:42px;font-size:13px">TEACHING</div>
  <div class="headline" style="left:3px;top:57px;font-size:11px">WORKPLACE</div>
  <div class="headline" style="left:3px;top:70px;font-size:17px">SKILLS</div>
  <ul class="bullets" style="left:3px;top:90px;font-size:6.5px;line-height:9px">
    <li>Covering Social Media.</li><li>Texting &amp; Cell Phones.</li><li>Grooming &amp; Hygiene.</li>
  </ul>
  <div class="btn btn-yellow" style="left:70px;top:108px;width:50px;height:11px;font-size:6.5px">Free Preview!</div>
</section>

<!-- Full banner 468x60, logo left -->
<section class="ad blue-field" style="left:598px;top:520px;width:468px;height:60px">
  <div class="white-field" style="left:0;top:0;width:75px;height:60px"></div>
  <div class="stripe" style="left:75px;top:0;width:6px;height:60px;background:var(--red)"></div>
  <div class="brand" style="left:0;top:16px;width:75px;font-size:11px">RIDGELINE<br>Academy</div>
  <div class="script" style="left:95px;top:4px;font-size:29px">Online Training</div>
  <div class="headline" style="left:86px;top:38px;font-size:14px">TEACHING WORKPLACE SKILLS</div>
  <ul class="bullets" style="left:283px;top:6px;font-size:11px;line-height:16px">
    <li>Covering Social Media.</li><li>Texting &amp; Cell Phones.</li><li>Grooming &amp; Hygiene.</li>
  </ul>
  <div class="btn btn-red" style="left:403px;top:8px;width:58px;height:44px;font-size:14px;white-space:normal;text-align:center;line-height:1.1">Free Preview!</div>
</section>

<!-- Full banner 468x60, logo right -->
<section class="ad blue-field" style="left:598px;top:592px;width:468px;height:60px">
  <svg style="left:0;top:0" width="468" height="60" viewBox="0 0 468 60" aria-hidden="true">
    <path d="M392 0 Q376 30 390 60 H468 V0Z" fill="#c2161e"/>
    <path d="M396 0 Q380 30 394 60 H468 V0Z" fill="#fff"/>
  </svg>
  <div class="script" style="left:10px;top:4px;font-size:29px">Online Training</div>
  <div class="headline" style="left:8px;top:36px;font-size:13.5px">TEACHING WORKPLACE SKILLS</div>
  <ul class="bullets" style="left:190px;top:6px;font-size:11px;line-height:16px">
    <li>Covering Social Media.</li><li>Texting &amp; Cell Phones.</li><li>Grooming &amp; Hygiene.</li>
  </ul>
  <div class="photo" role="img" aria-label="Group of smiling young students" style="left:302px;top:4px;width:88px;height:56px"></div>
  <div class="brand" style="left:402px;top:4px;width:62px;font-size:9px">RIDGELINE<br>Academy</div>
  <div class="btn btn-yellow" style="left:384px;top:38px;width:78px;height:15px;font-size:9px">Free Preview!</div>
</section>

<!-- Small web ad 120x90, red button -->
<section class="ad blue-field" style="left:83px;top:652px;width:120px;height:90px">
  <div class="script center" style="left:0;top:4px;width:120px;font-size:18px">Online Training</div>
  <div class="headline center" style="left:0;top:22px;width:120px;font-size:24px">TEACHING</div>
  <div class="headline center" style="left:0;top:51px;width:120px;font-size:11.5px">WORKPLACE SKILLS</div>
  <div class="white-field" style="left:0;top:82px;width:120px;height:8px"></div>
  <div class="btn btn-red" style="left:24px;top:69px;width:74px;height:16px;font-size:9.5px">Free Preview! <span class="arrow">&#10140;</span></div>
</section>

<!-- Small web ad 120x90, yellow button -->
<section class="ad blue-field" style="left:226px;top:652px;width:120px;height:90px">
  <div class="script center" style="left:0;top:4px;width:120px;font-size:18px">Online Training</div>
  <div class="headline center" style="left:0;top:22px;width:120px;font-size:24px">TEACHING</div>
  <div class="headline center" style="left:0;top:51px;width:120px;font-size:11.5px">WORKPLACE SKILLS</div>
  <div class="white-field" style="left:0;top:82px;width:120px;height:8px"></div>
  <div class="btn btn-yellow" style="left:24px;top:68px;width:70px;height:16px;font-size:9.5px">Free Preview!</div>
</section>

</body>
</html>
```